Mobility Trade and Aged Care products

a catalogue that can be printed and uploaded in a format to our web site. must be able to insert pages and remove as needed to kee up with our product range.
reference sites are:
www.tallowbyhealth.com
www.mobilitytrade.com.au

```html
<!DOCTYPE html>
<html lang="en">
<head>
<meta charset="utf-8">
<title>Mobility Trade – Catalogue Cover</title>
<link rel="stylesheet" href="https://fonts.googleapis.com/css2?family=Josefin+Sans:wght@400;600&display=swap">
<style>
  :root {
    --navy: #2b3a64;
    --cyan: #0ea0e2;
    --paper: #ffffff;
    --mist: #eceff1;
    --brand: #7b3f70;
    --tagline: #3d8fd6;
    --ink-light: #ffffff;
    --photo-light: #e9e6e2;
    --photo-mid: #c9c2ba;
  }
  html, body {
    margin: 0;
    padding: 0;
    width: 1200px;
    height: 789px;
    overflow: hidden;
    background: var(--paper);
  }
  .cover {
    position: relative;
    width: 1200px;
    height: 789px;
    overflow: hidden;
    font-family: "Josefin Sans", Arial, sans-serif;
  }
  .cover-art {
    position: absolute;
    inset: 0;
    width: 1200px;
    height: 789px;
    display: block;
  }
  .brand {
    position: absolute;
    left: 798px;
    top: 66px;
    margin: 0;
  }
  .brand-name {
    display: block;
    font-size: 46px;
    font-weight: 400;
    line-height: 1;
    color: var(--brand);
    letter-spacing: -0.5px;
  }
  .brand-tagline {
    display: block;
    margin-top: 4px;
    margin-left: 12px;
    font-size: 12px;
    color: var(--tagline);
  }
  .contact {
    position: absolute;
    left: 64px;
    top: 566px;
    color: var(--ink-light);
    font-size: 11.5px;
    line-height: 13px;
    font-style: normal;
  }
  .contact p { margin: 0 0 13px; }
  .contact-name { font-weight: 600; }
  .contact-row { display: flex; }
  .contact-label { width: 58px; }
</style>
</head>
<body>
<main class="cover">
  <svg class="cover-art" viewBox="0 0 1020 660" preserveAspectRatio="none" aria-hidden="false">
    <defs>
      <linearGradient id="mistFill" x1="0" y1="0" x2="1" y2="1">
        <stop offset="0" stop-color="#f6f7f8"/>
        <stop offset="1" stop-color="var(--mist)"/>
      </linearGradient>
      <linearGradient id="photoFill" x1="0" y1="0" x2="1" y2="0">
        <stop offset="0" stop-color="#eef0f1" stop-opacity="0"/>
        <stop offset="0.3" stop-color="var(--photo-light)"/>
        <stop offset="0.7" stop-color="var(--photo-mid)"/>
        <stop offset="1" stop-color="#d8c7b3"/>
      </linearGradient>
    </defs>
    <rect class="backdrop" width="1020" height="660" fill="url(#mistFill)"/>
    <rect class="cover-photo" x="380" y="150" width="640" height="450" fill="url(#photoFill)"
          role="img" aria-label="Photo: a woman in a wheelchair working at a laptop in a bright office while a colleague looks on"/>
    <path class="top-wave" d="M0,0 H1020 V182 C900,205 760,212 610,192 C450,170 260,105 0,112 Z" fill="var(--paper)"/>
    <path class="top-wave-line" d="M80,128 C260,100 430,160 600,188" fill="none" stroke="#ffffff" stroke-width="3" opacity="0.8"/>
    <path class="accent-band" d="M0,240 C200,225 330,300 440,395 C550,490 650,575 800,574 C900,573 980,568 1020,564 L1020,660 L0,660 Z" fill="var(--cyan)"/>
    <path class="navy-field" d="M0,258 C190,246 320,320 430,412 C540,505 650,590 800,589 C900,588 980,582 1020,577 L1020,660 L0,660 Z" fill="var(--navy)"/>
  </svg>

  <h1 class="brand">
    <span class="brand-name">Mobility Trade</span>
    <span class="brand-tagline">Sales, Service and Repairs</span>
  </h1>

  <address class="contact">
    <p><span class="contact-name">Mobility Trade</span><br>Unit 8 14 Elm Street, KINGSWOOD</p>
    <p>info@mobilitytrade.com.au</p>
    <p>
      <span class="contact-row"><span class="contact-label">Telephone</span>: +61 2 5550 1842</span>
      <span class="contact-row"><span class="contact-label">Mobile</span>: +61 400 555 718</span>
      <span class="contact-row"><span class="contact-label">Fax</span>: +61 2 5550 1843</span>
    </p>
    <p>www.mobilitytrade.com.au</p>
  </address>
</main>
</body>
</html>
```